Building company buisness cards

We are looking for a sharp modern new look for our business cards.We are a New Zealand based company that specialises in house and land packages.We have attached a photo of the current logo and would like to see if it can be improved somehow if needed.We are open to any colours but we have chosen Black and White at this stage. Feel free to change the font and make the logo smarter looking.Play with the colours and see what looks best.We want a card that looks so good know one will want to throw it away!

Target Market(s)

Building profesonals, home buyers

Industry/Entity Type

Building

Contact Information for Business Card

Derek Haskins
0274930268
derekh@stonerange.co.nz

Font styles to use
Serif
Sans Serif

Colors

Designer to choose colors to be used in the design.

Requirements
Must have
• Just the logo on one side and details on the other
• Clean simple looking card
Nice to have
• Round corners and detail like raised or spot UV
• Something that stands out
Should not have
• To title needed, Director etc

```html
<!DOCTYPE html>
<html lang="en">
<head>
<meta charset="utf-8">
<title>Stonerange business cards</title>
<link rel="stylesheet" href="https://fonts.googleapis.com/css2?family=Open+Sans:wght@300;400&display=swap">
<style>
  :root {
    --backdrop: #2a2a2a;
    --card: #1b1b1c;
    --card-edge: #0e0e0e;
    --gloss: #0a0a0a;
    --ink-light: #f2f2f2;
    --ink-soft: #d6d6d6;
  }
  * { margin: 0; padding: 0; box-sizing: border-box; }
  html, body {
    width: 1200px; height: 942px; overflow: hidden;
    background: var(--backdrop);
  }
  .sheet {
    position: relative; width: 1200px; height: 942px;
    display: flex; justify-content: center; align-items: center; gap: 80px;
  }
  .card {
    position: relative; width: 340px; height: 520px;
    background: var(--card);
    border-radius: 26px;
    box-shadow: 0 0 0 1px var(--card-edge), 0 18px 40px rgba(0,0,0,0.45);
    overflow: hidden;
  }
  .card-face {
    position: absolute; width: 520px; height: 340px;
    left: -90px; top: 90px;
    transform: rotate(90deg);
  }
  .company-name {
    font-family: "Open Sans", Arial, sans-serif;
    font-weight: 400; letter-spacing: 1px; line-height: 1;
    white-space: nowrap;
  }
  .card-front .company-name {
    position: absolute; left: 50%; top: 50%;
    transform: translate(-50%, -50%);
    font-size: 44px; color: var(--gloss);
  }
  .card-back .company-name {
    position: absolute; left: 48px; top: 104px;
    font-size: 38px; color: var(--ink-light);
  }
  .contact {
    position: absolute; left: 210px; top: 188px;
    font-family: "Open Sans", Arial, sans-serif; color: var(--ink-soft);
  }
  .contact-name {
    font-size: 20px; font-weight: 300; color: var(--ink-light);
    margin-bottom: 8px;
  }
  .contact-line {
    display: flex; align-items: center; gap: 8px;
    font-size: 14px; font-weight: 400; margin-bottom: 4px;
  }
  .contact-line svg { width: 12px; height: 12px; flex: none; }
</style>
</head>
<body>
<main class="sheet">
  <section class="card card-front" aria-label="Card front">
    <div class="card-face">
      <p class="company-name">Stonerange</p>
    </div>
  </section>

  <section class="card card-back" aria-label="Card back">
    <div class="card-face">
      <p class="company-name">Stonerange</p>
      <div class="contact">
        <p class="contact-name">Derek Haskins</p>
        <p class="contact-line">
          <svg viewBox="0 0 12 12" aria-hidden="true"><rect width="12" height="12" rx="1.5" fill="#d6d6d6"/><path d="M3.5 2.5h1.6l.7 2-1 .8a5 5 0 0 0 2 2l.8-1 2 .7v1.6A1 1 0 0 1 8.6 9.6 6.5 6.5 0 0 1 2.4 3.4a1 1 0 0 1 1.1-.9z" fill="#1b1b1c"/></svg>
          0274930268
        </p>
        <p class="contact-line">
          <svg viewBox="0 0 12 12" aria-hidden="true"><rect width="12" height="12" rx="1.5" fill="#d6d6d6"/><rect x="2.2" y="3.4" width="7.6" height="5.2" fill="none" stroke="#1b1b1c" stroke-width="1"/><path d="M2.2 3.4 6 6.4l3.8-3" fill="none" stroke="#1b1b1c" stroke-width="1"/></svg>
          derekh@stonerange.co.nz
        </p>
      </div>
    </div>
  </section>
</main>
</body>
</html>
```